Business Card Design Project for Web Development Company

Need a professional card that stands out with both color and texture.
We provide websites and web development services for small businesses with a focus on connections. Examples include: Automotive repair shop, we take their repair logs and make them available online so their customers can view, print and share (when selling) their maintenance records. Vet clinic, we create systems where customers can sign up for a recurring payment program for the annual wellness checks on their pets and get reminders when it's time, then see and schedule their own appointments. Etc... So not simply a website, but one that connects systems or customers to the business.
Important - !!!!We will be using http://inkvaleprinters.com/ for the cards, so take a look at what options are available for business card printing, they can do a lot of cool things!!!!
You can pick any 1-3 options from inkvaleprinters. I'm leaning towards a black background, but the logo will work on any color.
Front:
Marcus Telford
2750 SW 8th Ave STE 214-587
Alder Ridge, WA 98512
555-617-2038 - cell
555-259-7306 - office
marcus@sitelinkhub.com
www.SiteLinkHub.com
Updates
We provide websites and web development services for small businesses with a focus on connections. Examples include: Automotive repair shop, we take their repair logs and make them available online so their customers can view, print and share (when selling) their maintenance records. Vet clinic, we create systems where customers can sign up for a recurring payment program for the annual wellness checks on their pets and get reminders when it''s time, then see and schedule their own appointments. Etc... So not simply a website, but one that connects systems or customers to the business.
Target Market(s)
Small business owners
Industry/Entity Type
Automotive
Look and feel
Each slider illustrates characteristics of the customer's brand and the style your logo design should communicate.

```html
<!DOCTYPE html>
<html lang="en">
<head>
<meta charset="utf-8">
<title>SiteLinkHub Business Card</title>
<link rel="stylesheet" href="https://fonts.googleapis.com/css2?family=Mulish:wght@300;400;700;800&display=swap">
<style>
  :root {
    --backdrop: #7c7c7c;
    --card-dark: #262626;
    --card-front: #1e1e1e;
    --card-front-tone: #2a2a2a;
    --brand-blue: #2f9ee0;
    --name-grey: #b9b9b9;
    --detail-grey: #a9a9a9;
  }
  * { margin: 0; padding: 0; box-sizing: border-box; }
  html, body { width: 1200px; height: 1000px; overflow: hidden; }
  body {
    position: relative;
    background: var(--backdrop);
    font-family: "Mulish", sans-serif;
  }
  .card { position: absolute; width: 748px; height: 465px; overflow: hidden; }

  .card-front { left: 45px; top: 83px; }
  .card-front .texture-field {
    position: absolute; inset: 0;
    background: linear-gradient(135deg, var(--card-front-tone), var(--card-front));
  }
  .card-front .brand-name {
    position: absolute; left: 0; right: 0; top: 190px;
    text-align: center;
    font-size: 82px; font-weight: 800; letter-spacing: 1px;
    color: var(--brand-blue);
    line-height: 1;
  }

  .card-back {
    left: 395px; top: 447px;
    background: var(--card-dark);
  }
  .card-back .brand-vertical {
    position: absolute; left: 60px; top: 420px;
    transform: rotate(-90deg); transform-origin: 0 0;
    font-size: 52px; font-weight: 800; letter-spacing: 2px;
    color: var(--brand-blue);
    line-height: 1;
    white-space: nowrap;
  }
  .contact-block { position: absolute; left: 343px; top: 60px; color: var(--detail-grey); }
  .person-name {
    font-size: 36px; font-weight: 700; color: var(--name-grey);
    line-height: 1; margin-bottom: 34px;
  }
  .detail-group { font-size: 24px; font-weight: 300; line-height: 31px; margin-bottom: 32px; }
  .web-address {
    position: absolute; left: 343px; top: 390px;
    font-size: 24px; font-weight: 300; color: var(--detail-grey);
  }
</style>
</head>
<body>
  <section class="card card-front">
    <div class="texture-field" role="img" aria-label="Dark textured background with a repeating pattern of connected dots"></div>
    <div class="brand-name">SiteLinkHub</div>
  </section>

  <section class="card card-back">
    <div class="brand-vertical">SiteLinkHub</div>
    <div class="contact-block">
      <h1 class="person-name">Marcus Telford</h1>
      <p class="detail-group">2750 SW 8th Ave STE 214-587<br>Alder Ridge, WA 98512</p>
      <p class="detail-group">555-617-2038 - cell<br>555-259-7306 - office<br>marcus@sitelinkhub.com</p>
    </div>
    <p class="web-address">sitelinkhub.com</p>
  </section>
</body>
</html>
```